Brivora Works" Journey Check Kit" Instructions Cards

We need to design two 4.25" x 5.5" 2-sided COVID-19 Specimen Collection Instructions Cards. One card is for the collection and testing of RT-PCR Nasal Swab Specimen and the second card is for the collection and testing of a Rapid Antigen Nasal Swab specimen.

Each card will be 4.25" x 5.5", 2-sided, laminated no-edge seal, with 3 color front and 2 color back.

RT-PCR Nasal Swab Collection Kit Instructions:
1. Please see an "example only" of a collection test kit instructions done for PCR Saliva test (see attached 2-sided card).
2. Please see attached PDF of the RT-PCR Nasal Swab Collection instructions. We will need to follow these collection steps instructions but design our own illustrations. With this set of instructions we will have a total of 8 steps.
3. Please see our Nasal Swab Collection device (see attached images), as our nasal swab is a dry collection device.

Rapid Antigen Nasal Swab Collection Kit Instructions:
1. Please see an "example" of a collection test kit instructions done for Rapid Antigen Test (see attached image with instructions). we will need to follow these steps 7 steps and will revise/shorten the copy.
2. We will have a total of 8 steps and will provide detailed copy for each step.

Please email me with any questions you may have: tlindqvist@brivoraassays.example

Thank you

Tom

```html
<!DOCTYPE html>
<html lang="en">
<head>
<meta charset="utf-8">
<title>Brivora Works – Specimen Collection Instruction Cards</title>
<link href="https://fonts.googleapis.com/css2?family=Bebas+Neue&family=Open+Sans:wght@400;600;700&display=swap" rel="stylesheet">
<style>
  :root {
    --ink: #1f1f1f;
    --black: #111111;
    --pill: #2c2c2c;
    --green: #8dc63f;
    --blue: #5567b1;
    --navy: #3f4f9c;
    --tan: #d3c9b6;
    --paper: #ffffff;
    --hex-light: #f4f4f4;
    --hex-mid: #e3e3e3;
    --dot: #5a67b8;
    --stage: #ffffff;
  }
  * { box-sizing: border-box; margin: 0; padding: 0; }
  html, body { width: 910px; height: 1200px; overflow: hidden; background: var(--stage); }
  body { position: relative; font-family: "Open Sans", sans-serif; color: var(--ink); }

  .card {
    position: absolute; top: 328px; width: 420px; height: 544px;
    background: var(--paper); overflow: hidden;
    box-shadow: 0 2px 10px rgba(0,0,0,.18);
  }
  .card--antigen { left: 20px; }
  .card--pcr { left: 470px; }

  .card__header {
    position: absolute; left: 0; top: 0; width: 100%; height: 84px;
    background: radial-gradient(ellipse at center, var(--hex-light) 0%, var(--hex-mid) 100%);
  }
  .brand {
    position: absolute; left: 0; top: 0; width: 100%; height: 84px;
    display: flex; align-items: center; justify-content: center; gap: 10px;
  }
  .brand__mark { width: 18px; height: 18px; border-radius: 50%; background: var(--navy); }
  .brand__name {
    font-family: "Open Sans", sans-serif; font-weight: 600; font-size: 25px;
    color: var(--ink); letter-spacing: .5px;
  }

  /* Antigen card */
  .intro { position: absolute; left: 0; top: 84px; width: 100%; height: 94px; }
  .intro__panel { position: absolute; left: 0; top: 0; width: 212px; height: 94px; background: var(--green); }
  .intro__count {
    position: absolute; left: 27px; top: 10px;
    font-family: "Bebas Neue", sans-serif; font-size: 38px; line-height: 1; color: var(--ink);
  }
  .intro__title {
    position: absolute; left: 27px; top: 44px;
    font-family: "Bebas Neue", sans-serif; font-size: 22px; line-height: 1; color: #fff; letter-spacing: .3px;
  }
  .intro__email {
    position: absolute; left: 26px; top: 66px; width: 176px; height: 15px;
    border-radius: 8px; background: var(--navy); color: #fff;
    font-family: "Bebas Neue", sans-serif; font-size: 10px; line-height: 15px; text-align: center; letter-spacing: .2px;
  }
  .intro__photo {
    position: absolute; left: 212px; top: 0; width: 208px; height: 94px;
    background: linear-gradient(90deg, #d8cdb8 0%, #cfc2a9 35%, #c8532d 50%, #cfc2a9 65%, #d8cdb8 100%);
  }

  .steps { position: absolute; left: 13px; top: 204px; width: 393px; height: 331px; }
  .steps__spine {
    position: absolute; left: 0; top: 0; width: 52px; height: 100%;
    background: var(--black); border-radius: 28px 0 0 28px;
  }
  .steps__spine-label {
    position: absolute; left: 26px; top: 50%; transform: translate(-50%, -50%) rotate(-90deg);
    white-space: nowrap; font-family: "Bebas Neue", sans-serif; font-size: 19px; color: #fff; letter-spacing: .4px;
  }
  .steps__body {
    position: absolute; left: 46px; top: 0; width: 347px; height: 100%;
    background: var(--tan); border-radius: 0 24px 0 0;
  }
  .step {
    position: absolute; left: 46px; width: 347px; height: 47.3px;
    border-bottom: 1px solid rgba(255,255,255,.6);
  }
  .step:last-child { border-bottom: none; }
  .step__num {
    position: absolute; left: 0; top: 0; width: 76px; height: 100%;
    clip-path: polygon(0 0, 100% 0, 80% 26%, 80% 100%, 0 100%);
    color: #fff; text-align: center; padding-right: 15px;
  }
  .step:nth-of-type(odd) .step__num { background: var(--blue); }
  .step:nth-of-type(even) .step__num { background: var(--green); }
  .step__label { display: block; font-family: "Bebas Neue", sans-serif; font-size: 8px; line-height: 1; padding-top: 6px; }
  .step__digits { display: block; font-family: "Bebas Neue", sans-serif; font-size: 24px; line-height: 1; }
  .step__text {
    position: absolute; left: 86px; top: 8px; width: 200px;
    font-size: 7.4px; line-height: 1.22; color: var(--ink);
  }
  .step__icon {
    position: absolute; right: 18px; top: 10px; width: 28px; height: 28px; border-radius: 6px;
    background: linear-gradient(135deg, #e9e3d6, #bfb6a4);
  }

  /* PCR card */
  .title-band { position: absolute; left: 0; top: 84px; width: 100%; height: 75px; background: var(--black); }
  .title-band__pill {
    position: absolute; left: 38px; top: 0; width: 344px; height: 75px;
    background: var(--pill); border-radius: 38px; text-align: center;
    font-family: "Bebas Neue", sans-serif; font-size: 35px; line-height: 32px; padding-top: 6px;
  }
  .title-band__line1 { display: block; color: #fff; }
  .title-band__line2 { display: block; color: var(--green); }
  .drops { position: absolute; top: 30px; width: 16px; height: 16px; }
  .drops--left { left: 10px; }
  .drops--right { right: 10px; }

  .instruction {
    position: absolute; left: 85px; width: 237px;
    border-top: 1.5px dotted var(--dot); border-bottom: 1.5px dotted var(--dot); border-left: 1.5px dotted var(--dot);
    display: flex; align-items: center;
    font-size: 7.3px; line-height: 1.2; color: var(--ink); padding: 0 8px;
  }
  .instruction--left { text-align: left; }
  .instruction--right { text-align: right; justify-content: flex-end; }
  .pictogram {
    position: absolute; width: 58px; height: 58px; border-radius: 50%;
    border: 1.5px dashed var(--green);
    background: radial-gradient(circle, #eef1fb 0%, #ffffff 75%);
  }
</style>
</head>
<body>

<section class="card card--antigen" aria-label="Rapid antigen instruction card">
  <div class="card__header" role="img" aria-label="Soft grey hexagon texture"></div>
  <div class="brand"><span class="brand__mark"></span><span class="brand__name">BRIVORA WORKS</span></div>

  <div class="intro">
    <div class="intro__panel">
      <div class="intro__count">7 STEPS</div>
      <div class="intro__title">RAPID ANTIGEN TEST</div>
      <div class="intro__email">TLINDQVIST@BRIVORAASSAYS.EXAMPLE</div>
    </div>
    <div class="intro__photo" role="img" aria-label="Photo of a specimen bag with biohazard label and packaged swab"></div>
  </div>

  <div class="steps">
    <div class="steps__spine"><span class="steps__spine-label">RAPID ANTIGEN NASAL SWAB SPECIMEN</span></div>
    <div class="steps__body"></div>

    <div class="step" style="top:0">
      <div class="step__num"><span class="step__label">STEP</span><span class="step__digits">01</span></div>
      <p class="step__text">It is a long established fact that a reader will be distracted by the readable content of a page when looking at its layout.</p>
      <div class="step__icon" role="img" aria-label="Icon of the test kit box"></div>
    </div>
    <div class="step" style="top:47.3px">
      <div class="step__num"><span class="step__label">STEP</span><span class="step__digits">02</span></div>
      <p class="step__text">It is a long established fact that a reader will be distracted by the readable content of a page when looking at its layout.</p>
      <div class="step__icon" role="img" aria-label="Icon of swab at the nostril"></div>
    </div>
    <div class="step" style="top:94.6px">
      <div class="step__num"><span class="step__label">STEP</span><span class="step__digits">03</span></div>
      <p class="step__text">It is a long established fact that a reader will be distracted by the readable content of a page when looking at its layout.</p>
      <div class="step__icon" role="img" aria-label="Icon of a swab"></div>
    </div>
    <div class="step" style="top:141.9px">
      <div class="step__num"><span class="step__label">STEP</span><span class="step__digits">04</span></div>
      <p class="step__text">It is a long established fact that a reader will be distracted by the readable content of a page when looking at its layout.</p>
      <div class="step__icon" role="img" aria-label="Icon of swab in extraction tube"></div>
    </div>
    <div class="step" style="top:189.2px">
      <div class="step__num"><span class="step__label">STEP</span><span class="step__digits">05</span></div>
      <p class="step__text">It is a long established fact that a reader will be distracted by the readable content of a page when looking at its layout.</p>
      <div class="step__icon" role="img" aria-label="Icon of dropper tube"></div>
    </div>
    <div class="step" style="top:236.5px">
      <div class="step__num"><span class="step__label">STEP</span><span class="step__digits">06</span></div>
      <p class="step__text">It is a long established fact that a reader will be distracted by the readable content of a page when looking at its layout.</p>
      <div class="step__icon" role="img" aria-label="Icon of drops on the test cassette"></div>
    </div>
    <div class="step" style="top:283.8px">
      <div class="step__num"><span class="step__label">STEP</span><span class="step__digits">07</span></div>
      <p class="step__text">It is a long established fact that a reader will be distracted by the readable content of a page when looking at its layout.</p>
      <div class="step__icon" role="img" aria-label="Icon of a timer"></div>
    </div>
  </div>
</section>

<section class="card card--pcr" aria-label="RT-PCR nasal swab instruction card">
  <div class="card__header" role="img" aria-label="Soft grey hexagon texture"></div>
  <div class="brand"><span class="brand__mark"></span><span class="brand__name">BRIVORA WORKS</span></div>

  <div class="title-band">
    <svg class="drops drops--left" viewBox="0 0 16 16" aria-hidden="true"><circle cx="8" cy="4" r="3" fill="#777"/><circle cx="4" cy="12" r="3" fill="#777"/><circle cx="12" cy="12" r="3" fill="#777"/></svg>
    <div class="title-band__pill">
      <span class="title-band__line1">RT-PCR NASAL</span>
      <span class="title-band__line2">SWAB SPECIMEN</span>
    </div>
    <svg class="drops drops--right" viewBox="0 0 16 16" aria-hidden="true"><circle cx="8" cy="4" r="3" fill="#777"/><circle cx="4" cy="12" r="3" fill="#777"/><circle cx="12" cy="12" r="3" fill="#777"/></svg>
  </div>

  <p class="instruction instruction--left" style="top:179px;height:43px">Remove Contents Where you will open the collection kit. Remove &amp; lay out contents of kit. Read instructions before starting specimen collection.</p>
  <p class="instruction instruction--right" style="top:234px;height:43px">Remove the swab from the package. Do not touch the soft end with your hands or anything else.</p>
  <p class="instruction instruction--left" style="top:289px;height:51px">Insert &amp; slowly rotate the swab, gently pressing against the inside of each nostril at least 4 times for a total of 15 seconds. Get as much nasal discharge as possible on the soft end of the swab.</p>
  <p class="instruction instruction--right" style="top:352px;height:54px">Place the swab in the sterile tube and snap off the end of the swab at the break line, so that it fits comfortably in the tube. Place the cap on the tube and screw down tightly to prevent leakage.</p>
  <p class="instruction instruction--left" style="top:423px;height:30px">Ently remove he swab.</p>
  <p class="instruction instruction--right" style="top:468px;height:55px">Place the tube | containing the swab in the biohazard bag provided and seal the bag. and follow the | instructions on the card for shipping to lab for testing.</p>

  <div class="pictogram" style="left:19px;top:174px" role="img" aria-label="Illustration of collection kit contents"></div>
  <div class="pictogram" style="left:342px;top:225px" role="img" aria-label="Illustration of the swab and tube"></div>
  <div class="pictogram" style="left:19px;top:287px" role="img" aria-label="Illustration of swabbing the nostril"></div>
  <div class="pictogram" style="left:342px;top:350px" role="img" aria-label="Illustration of nose with swab"></div>
  <div class="pictogram" style="left:19px;top:410px" role="img" aria-label="Illustration of specimen tubes"></div>
  <div class="pictogram" style="left:342px;top:467px" role="img" aria-label="Illustration of sealed sample tube"></div>
</section>

</body>
</html>
```